Business Card cabinets and cabinets components making company.

the card should be formal and interesting at the same time. The main colors will be black and white.

Font styles to use
Sans Serif

Colors

Designer to choose only greyscale colors for use in the design.

Requirements
Must have
• At least must have the followings:
office phone
cell phone
address
position
name
email
web

```html
<!DOCTYPE html>
<html lang="en">
<head>
<meta charset="utf-8">
<title>Trimwell Business Card</title>
<link rel="stylesheet" href="https://fonts.googleapis.com/css2?family=Montserrat:wght@400;700;800&display=swap">
<style>
  :root {
    --stage: #2a2a2a;
    --card: #121212;
    --card-edge: #1e1e1e;
    --ink-light: #ffffff;
    --ink-soft: #e6e6e6;
    --ink-dark: #111111;
    --rule: #8a8a8a;
  }
  * { box-sizing: border-box; margin: 0; padding: 0; }
  html, body { width: 1200px; height: 988px; overflow: hidden; }
  body {
    background: radial-gradient(ellipse at 50% 40%, #333 0%, var(--stage) 60%, #1c1c1c 100%);
    font-family: "Montserrat", sans-serif;
    color: var(--ink-light);
    position: relative;
  }
  .card {
    position: absolute;
    left: 250px;
    width: 700px;
    height: 400px;
    background: linear-gradient(160deg, #1a1a1a 0%, var(--card) 55%, #0c0c0c 100%);
    border-radius: 26px;
    border: 1px solid var(--card-edge);
    box-shadow: 0 18px 40px rgba(0,0,0,.55);
    overflow: hidden;
  }
  .card--front { top: 60px; }
  .card--back { top: 520px; }

  .brand {
    position: absolute;
    display: flex;
    align-items: center;
    gap: 14px;
    font-weight: 800;
    color: var(--ink-light);
    letter-spacing: -1px;
  }
  .brand__mark {
    width: 0.6em; height: 0.6em;
    border: 0.09em solid var(--ink-light);
  }
  .card--front .brand {
    font-size: 80px;
    left: 50%; top: 50%;
    transform: translate(-50%, -50%);
  }
  .card--back .brand {
    font-size: 62px;
    left: 50%; top: 50px;
    transform: translateX(-50%);
  }

  .person {
    position: absolute;
    left: 70px; top: 218px;
    width: 260px;
    text-align: right;
  }
  .person__name {
    font-weight: 700;
    font-size: 27px;
    letter-spacing: 1.5px;
  }
  .person__role {
    font-size: 17px;
    color: var(--ink-soft);
    margin-top: 4px;
  }
  .divider {
    position: absolute;
    left: 360px; top: 180px;
    width: 1px; height: 128px;
    background: var(--rule);
  }
  .contacts {
    position: absolute;
    left: 384px; top: 182px;
    list-style: none;
    font-size: 17px;
    line-height: 31px;
    color: var(--ink-soft);
  }
  .contacts li { display: flex; align-items: center; gap: 10px; }
  .contacts svg { width: 15px; height: 15px; fill: var(--ink-light); flex: none; }

  .address-band {
    position: absolute;
    left: 0; right: 0; bottom: 30px;
    height: 44px;
    background: var(--ink-light);
    color: var(--ink-dark);
    font-size: 19px;
    display: flex;
    align-items: center;
    justify-content: center;
  }
</style>
</head>
<body>

<section class="card card--front" aria-label="Card front">
  <div class="brand"><span class="brand__mark"></span>Trimwell</div>
</section>

<section class="card card--back" aria-label="Card back">
  <div class="brand"><span class="brand__mark"></span>Trimwell</div>

  <div class="person">
    <p class="person__name">DORIAN HALE</p>
    <p class="person__role">Owner/CEO</p>
  </div>

  <div class="divider"></div>

  <ul class="contacts">
    <li>
      <svg viewBox="0 0 24 24" aria-hidden="true"><path d="M6.6 10.8a15.1 15.1 0 0 0 6.6 6.6l2.2-2.2c.3-.3.7-.4 1-.2 1.1.4 2.3.6 3.6.6.6 0 1 .4 1 1V20c0 .6-.4 1-1 1A17 17 0 0 1 3 4c0-.6.4-1 1-1h3.5c.6 0 1 .4 1 1 0 1.3.2 2.5.6 3.6.1.3 0 .7-.2 1z"/></svg>
      555-210-4836
    </li>
    <li>
      <svg viewBox="0 0 24 24" aria-hidden="true"><path d="M7 1h10a2 2 0 0 1 2 2v18a2 2 0 0 1-2 2H7a2 2 0 0 1-2-2V3a2 2 0 0 1 2-2zm0 3v14h10V4zm5 15.5a1 1 0 1 0 0 2 1 1 0 0 0 0-2z"/></svg>
      5550 987 321
    </li>
    <li>
      <svg viewBox="0 0 24 24" aria-hidden="true"><path d="M2 5h20v14H2zm2 2v.4l8 5.2 8-5.2V7zm0 2.8V17h16V9.8l-8 5.2z"/></svg>
      info@trimwell.com
    </li>
    <li>
      <svg viewBox="0 0 24 24" aria-hidden="true"><path d="M12 2a10 10 0 1 0 0 20 10 10 0 0 0 0-20zm0 2c.9 0 2.2 1.9 2.8 5H9.2C9.8 5.9 11.1 4 12 4zm-3 7h6a16 16 0 0 1 0 2H9a16 16 0 0 1 0-2zm-4.9 0H7a18 18 0 0 0 0 2H4.1a8 8 0 0 1 0-2zm12.9 0h2.9a8 8 0 0 1 0 2H17a18 18 0 0 0 0-2zm-7.8 4h5.6c-.6 3.1-1.9 5-2.8 5s-2.2-1.9-2.8-5z"/></svg>
      www.trimwell.com
    </li>
  </ul>

  <div class="address-band">1450 W Alder street Marlow County name 4187</div>
</section>

</body>
</html>
```